Building company buisness cards

We are looking for a sharp modern new look for our business cards.
We are a New Zealand based company that specialises in house and land packages.
We have attached a photo of the current logo and would like to see if it can be improved somehow if needed.
We are open to any colours but we have chosen green at this stage.
Feel free to change the font and make the logo smarter looking.
Play with the colours and see what looks best.

We want a card that looks so good know one will want to throw it away!

Target Market(s)

Home buyers

Industry/Entity Type

Building

Contact Information for Business Card

Dorian Keswick
0217392604
dkeswick@tidewellhomecraft.co.nz
tidewellhomecraft.co.nz

Font styles to use
Serif
Sans Serif

Colors

Designer to choose colors to be used in the design.

Requirements
Must have
• Logo and company name on one side, details on the other side
Nice to have
• Color codes for the original green are HEX #4a8028, RGB(74,128,40), CMYK(42,0,69,50)
• Round corners, Raised and/or spot UV

```html
<!DOCTYPE html>
<html lang="en">
<head>
<meta charset="utf-8">
<title>Tidewell Homecraft – Business Cards</title>
<link rel="stylesheet" href="https://fonts.googleapis.com/css2?family=Fira+Sans:wght@700;800&family=Arimo:wght@400;700&display=swap">
<style>
  :root {
    --page: #f1efea;
    --roof-green: #217012;
    --card-white: #ffffff;
    --ink: #2b2b2b;
    --band-shade: rgba(0, 0, 0, 0.28);
  }
  * { margin: 0; padding: 0; box-sizing: border-box; }
  html, body {
    width: 1175px;
    height: 1200px;
    overflow: hidden;
    background: var(--page);
  }
  .stage {
    position: relative;
    width: 1175px;
    height: 1200px;
  }
  .card {
    position: absolute;
    width: 751px;
    height: 427px;
    display: block;
    box-shadow: 0 4px 10px rgba(0, 0, 0, 0.22);
  }
  .card--front { left: 128px; top: 146px; }
  .card--back  { left: 294px; top: 634px; }

  .card__field--green { fill: var(--roof-green); }
  .card__field--white { fill: var(--card-white); }
  .roof-band--white { fill: var(--card-white); }
  .roof-band--green { fill: var(--roof-green); }

  .brand-name {
    font-family: "Fira Sans", sans-serif;
    font-weight: 800;
    font-size: 44px;
    letter-spacing: 1px;
    fill: var(--card-white);
  }
  .brand-mark { fill: var(--card-white); }
  .front-url {
    font-family: "Arimo", sans-serif;
    font-size: 26px;
    fill: var(--card-white);
  }
  .contact-name {
    font-family: "Arimo", sans-serif;
    font-weight: 700;
    font-size: 28px;
    fill: var(--roof-green);
  }
  .contact-line {
    font-family: "Arimo", sans-serif;
    font-size: 21px;
    fill: var(--ink);
  }
</style>
</head>
<body>
<main class="stage">

  <svg class="card card--front" viewBox="0 0 695 395" role="group" aria-label="Card front: Tidewell Homecraft">
    <defs>
      <filter id="band-shadow" x="-10%" y="-10%" width="120%" height="130%">
        <feDropShadow dx="0" dy="5" stdDeviation="5" flood-color="#000" flood-opacity="0.3"/>
      </filter>
    </defs>
    <rect class="card__field--green" width="695" height="395"/>
    <path class="roof-band--white" filter="url(#band-shadow)"
          d="M0,190 L272,0 L437,0 L695,175 L695,270 L400,62 Q352,28 304,62 L0,275 Z"/>
    <circle class="brand-mark" cx="347" cy="150" r="34"/>
    <text class="brand-name" x="347" y="268" text-anchor="middle">TIDEWELL HOMECRAFT</text>
    <text class="front-url" x="347" y="342" text-anchor="middle">tidewellhomecraft.co.nz</text>
  </svg>

  <svg class="card card--back" viewBox="0 0 695 395" role="group" aria-label="Card back: contact details">
    <defs>
      <filter id="band-shadow-back" x="-10%" y="-10%" width="120%" height="130%">
        <feDropShadow dx="0" dy="5" stdDeviation="5" flood-color="#000" flood-opacity="0.3"/>
      </filter>
    </defs>
    <rect class="card__field--white" width="695" height="395"/>
    <path class="roof-band--green" filter="url(#band-shadow-back)"
          d="M0,189 L273,0 L440,0 L695,179 L695,269 L404,58 Q356,24 308,58 L0,274 Z"/>
    <text class="contact-name" x="340" y="172" text-anchor="middle">Dorian Keswick</text>
    <text class="contact-line" x="347" y="246" text-anchor="middle">0217392604</text>
    <text class="contact-line" x="347" y="284" text-anchor="middle">dkeswick@tidewellhomecraft.co.nz</text>
    <text class="contact-line" x="347" y="323" text-anchor="middle">tidewellhomecraft.co.nz</text>
  </svg>

</main>
</body>
</html>
```